OKU Consulting Firm needs artwork for foyer

We are looking for a piece of artwork for our foyer entrance. It will be displayed on the white wall above the two armchairs.

The piece could be meaningful to our organisation, but also could be of an abstract nature. We want the artwork to be striking/interesting as it is displayed in the foyer. The artwork would be printed on a landscape canvas print with dimensions 76 cm x 152 cm.

Please see attached word document "Brisk Lantern" for all specifications.

Target Market(s)

Industry/Entity Type

Consulting

Requirements
Must have
• Please see attached word document "Brisk Lantern" for all specifications.
Nice to have
Should not have

```html
<!DOCTYPE html>
<html lang="en">
<head>
<meta charset="utf-8">
<title>OKU Consulting Firm — Foyer Word Artwork</title>
<link rel="stylesheet" href="https://fonts.googleapis.com/css2?family=Oranienbaum&display=swap">
<style>
  :root {
    --canvas-bg: #f5f6f6;
    --ink-black: #111111;
    --ink-grey: #808285;
    --ink-charcoal: #5a5b5d;
    --ink-silver: #c2c3c4;
    --ink-cyan: #00bcd4;
    --ink-sky: #5ab8ee;
    --ink-blue: #1b78bf;
  }
  html, body {
    margin: 0;
    padding: 0;
    width: 1200px;
    height: 698px;
    overflow: hidden;
    background: var(--canvas-bg);
  }
  .word-cloud {
    display: block;
    width: 1200px;
    height: 698px;
    font-family: "Oranienbaum", "Bodoni Moda", serif;
  }
  .black { fill: var(--ink-black); }
  .grey { fill: var(--ink-grey); }
  .charcoal { fill: var(--ink-charcoal); }
  .silver { fill: var(--ink-silver); }
  .cyan { fill: var(--ink-cyan); }
  .sky { fill: var(--ink-sky); }
  .blue { fill: var(--ink-blue); }
</style>
</head>
<body>
<svg class="word-cloud" viewBox="0 0 1500 873" xmlns="http://www.w3.org/2000/svg" role="img" aria-label="Word cloud of OKU Consulting Firm values">
  <rect width="1500" height="873" fill="var(--canvas-bg)"/>

  <!-- Band 1 -->
  <text class="black" x="70" y="140" font-size="110" textLength="600" lengthAdjust="spacingAndGlyphs">collaboration</text>
  <text class="silver" x="700" y="140" font-size="110" textLength="280" lengthAdjust="spacingAndGlyphs">nimble</text>
  <text class="blue" x="1010" y="70" font-size="28" textLength="130" lengthAdjust="spacingAndGlyphs">healthcare</text>
  <text class="black" x="1160" y="70" font-size="28" textLength="130" lengthAdjust="spacingAndGlyphs">consulting</text>
  <text class="cyan" x="1310" y="70" font-size="28" textLength="110" lengthAdjust="spacingAndGlyphs">positive</text>
  <text class="blue" x="1010" y="105" font-size="28" textLength="160" lengthAdjust="spacingAndGlyphs">development</text>
  <text class="silver" x="1190" y="105" font-size="28" textLength="140" lengthAdjust="spacingAndGlyphs">evaluation</text>
  <text class="cyan" x="1350" y="105" font-size="28" textLength="60" lengthAdjust="spacingAndGlyphs">OKU</text>
  <text class="silver" x="1010" y="140" font-size="28" textLength="140" lengthAdjust="spacingAndGlyphs">supportive</text>
  <text class="grey" x="1170" y="140" font-size="28" textLength="110" lengthAdjust="spacingAndGlyphs">integrity</text>
  <text class="sky" x="1300" y="140" font-size="28" textLength="90" lengthAdjust="spacingAndGlyphs">nimble</text>

  <!-- Band 2 -->
  <text class="cyan" x="70" y="290" font-size="170" textLength="500" lengthAdjust="spacingAndGlyphs">quality</text>
  <text class="grey" x="600" y="290" font-size="170" textLength="420" lengthAdjust="spacingAndGlyphs">growth</text>
  <text class="black" x="1050" y="200" font-size="32" textLength="200" lengthAdjust="spacingAndGlyphs">administration</text>
  <text class="black" x="1270" y="200" font-size="32" textLength="90" lengthAdjust="spacingAndGlyphs">quality</text>
  <text class="sky" x="1050" y="240" font-size="32" textLength="190" lengthAdjust="spacingAndGlyphs">collaboration</text>
  <text class="grey" x="1260" y="240" font-size="32" textLength="90" lengthAdjust="spacingAndGlyphs">growth</text>
  <text class="cyan" x="1370" y="240" font-size="32" textLength="55" lengthAdjust="spacingAndGlyphs">OKU</text>
  <text class="sky" x="1050" y="280" font-size="32" textLength="130" lengthAdjust="spacingAndGlyphs">specialist</text>
  <text class="cyan" x="1200" y="280" font-size="32" textLength="140" lengthAdjust="spacingAndGlyphs">responsive</text>
  <text class="sky" x="1050" y="320" font-size="32" textLength="110" lengthAdjust="spacingAndGlyphs">advisory</text>
  <text class="grey" x="1180" y="320" font-size="32" textLength="140" lengthAdjust="spacingAndGlyphs">excellence</text>
  <text class="cyan" x="1340" y="320" font-size="32" textLength="85" lengthAdjust="spacingAndGlyphs">people</text>

  <!-- Band 3 -->
  <text class="black" x="70" y="530" font-size="250" textLength="675" lengthAdjust="spacingAndGlyphs">people</text>
  <text class="sky" x="780" y="362" font-size="22" textLength="65" lengthAdjust="spacingAndGlyphs">nimble</text>
  <text class="silver" x="865" y="362" font-size="22" textLength="90" lengthAdjust="spacingAndGlyphs">supportive</text>
  <text class="black" x="975" y="362" font-size="22" textLength="90" lengthAdjust="spacingAndGlyphs">consulting</text>
  <text class="blue" x="1085" y="362" font-size="22" textLength="90" lengthAdjust="spacingAndGlyphs">healthcare</text>
  <text class="blue" x="1195" y="362" font-size="22" textLength="105" lengthAdjust="spacingAndGlyphs">development</text>
  <text class="cyan" x="1320" y="362" font-size="22" textLength="85" lengthAdjust="spacingAndGlyphs">innovaton</text>
  <text class="cyan" x="780" y="500" font-size="170" textLength="612" lengthAdjust="spacingAndGlyphs">integrity</text>
  <text class="sky" x="780" y="575" font-size="30" textLength="170" lengthAdjust="spacingAndGlyphs">collaboration</text>
  <text class="cyan" x="970" y="575" font-size="30" textLength="110" lengthAdjust="spacingAndGlyphs">positive</text>
  <text class="black" x="1100" y="575" font-size="30" textLength="90" lengthAdjust="spacingAndGlyphs">quality</text>
  <text class="grey" x="1210" y="575" font-size="30" textLength="90" lengthAdjust="spacingAndGlyphs">growth</text>
  <text class="cyan" x="1320" y="575" font-size="30" textLength="60" lengthAdjust="spacingAndGlyphs">OKU</text>

  <!-- Band 4 -->
  <text class="cyan" x="70" y="690" font-size="120" textLength="216" lengthAdjust="spacingAndGlyphs">OKU</text>
  <text class="grey" x="310" y="690" font-size="120" textLength="504" lengthAdjust="spacingAndGlyphs">responsive</text>
  <text class="sky" x="840" y="690" font-size="120" textLength="400" lengthAdjust="spacingAndGlyphs">advisory</text>
  <text class="cyan" x="1275" y="630" font-size="26" textLength="120" lengthAdjust="spacingAndGlyphs">innovaton</text>
  <text class="cyan" x="1275" y="665" font-size="26" textLength="85" lengthAdjust="spacingAndGlyphs">people</text>
  <text class="silver" x="1275" y="700" font-size="26" textLength="130" lengthAdjust="spacingAndGlyphs">evaluation</text>

  <!-- Band 5 -->
  <text class="black" x="70" y="820" font-size="100" textLength="588" lengthAdjust="spacingAndGlyphs">accountability</text>
  <text class="blue" x="690" y="820" font-size="100" textLength="400" lengthAdjust="spacingAndGlyphs">specialist</text>
  <text class="silver" x="1110" y="820" font-size="80" textLength="330" lengthAdjust="spacingAndGlyphs">evaluation</text>
</svg>
</body>
</html>
```